Business card design needed

My company specialises in carpentry and building services.
Based in Brisbane QLD
We also do:
property maintenance
plastering
painting
tiling
property maintenance

Industry/Entity Type

Carpentry

Contact Information for Business Card

ND Services QLD
Neil 0412555783
Derek 0493721068

```html
<!DOCTYPE html>
<html lang="en">
<head>
<meta charset="utf-8">
<title>ND Services QLD – Business Card</title>
<link rel="stylesheet" href="https://fonts.googleapis.com/css2?family=Arimo:wght@400;500&display=swap">
<style>
  :root {
    --page-bg: #ffffff;
    --card-light: #f4f4f4;
    --card-mid: #b5b5b5;
    --card-dark: #7c7c7c;
    --band: #333333;
    --band-text: #ffffff;
    --band-muted: #cfcfcf;
    --ink-soft: #6e6e6e;
    --ink: #454545;
    --mark: #6a6a6a;
    --mark-fill: #eeeeee;
    --note: #666666;
  }
  html, body {
    margin: 0;
    padding: 0;
    width: 1200px;
    height: 1000px;
    overflow: hidden;
    background: var(--page-bg);
    font-family: "Arimo", Arial, sans-serif;
  }
  .canvas {
    position: relative;
    width: 1200px;
    height: 1000px;
  }
  .business-card {
    position: absolute;
    left: 77px;
    top: 56px;
    width: 1063px;
    height: 614px;
    background: radial-gradient(ellipse 560px 420px at 531px 170px,
      var(--card-light) 0%, #e2e2e2 30%, var(--card-mid) 65%, var(--card-dark) 100%);
    overflow: hidden;
  }
  .card-logo {
    position: absolute;
    left: 374px;
    top: 75px;
    width: 314px;
    height: 314px;
  }
  .card-logo svg { display: block; }
  .services-title,
  .services-list {
    position: absolute;
    left: 0;
    width: 100%;
    text-align: center;
    margin: 0;
    text-transform: uppercase;
  }
  .services-title {
    top: 425px;
    font-size: 24px;
    font-weight: 500;
    color: var(--ink-soft);
    letter-spacing: 0.5px;
  }
  .services-list {
    top: 462px;
    font-size: 21px;
    color: var(--ink);
    letter-spacing: 0.5px;
  }
  .contact-band {
    position: absolute;
    left: 0;
    bottom: 0;
    width: 100%;
    height: 115px;
    background: var(--band);
    text-align: center;
    text-transform: uppercase;
  }
  .contact-numbers {
    margin: 10px 0 0;
    font-size: 21px;
    font-weight: 500;
    color: var(--band-text);
    letter-spacing: 1px;
  }
  .contact-numbers .divider {
    display: inline-block;
    width: 1px;
    height: 26px;
    background: #666;
    vertical-align: middle;
    margin: 0 14px 0 12px;
  }
  .location {
    margin: 9px 0 0;
    font-size: 17px;
    color: var(--band-muted);
    letter-spacing: 1.5px;
  }
  .presentation-notes {
    position: absolute;
    left: 175px;
    top: 768px;
    width: 420px;
    text-align: center;
    font-size: 22px;
    color: var(--note);
    letter-spacing: 1px;
    text-transform: uppercase;
    line-height: 34px;
  }
  .presentation-notes p { margin: 0 0 32px; }
  .logo-badge {
    position: absolute;
    left: 662px;
    top: 636px;
    width: 310px;
    height: 310px;
  }
</style>
</head>
<body>
<main class="canvas">
  <section class="business-card">
    <div class="card-logo">
      <svg width="314" height="314" viewBox="0 0 314 314">
        <circle cx="157" cy="157" r="155" fill="none" stroke="var(--mark)" stroke-width="2"/>
        <text x="157" y="166" text-anchor="middle" font-family="Arimo, Arial, sans-serif"
              font-size="30" font-weight="500" fill="var(--mark)" letter-spacing="1">ND SERVICES QLD</text>
      </svg>
    </div>
    <h1 class="services-title">Carpentry and Building Services</h1>
    <p class="services-list">Property Maintenance I Plastering I Painting I Tiling</p>
    <div class="contact-band">
      <p class="contact-numbers">Neil 0412555783<span class="divider"></span>Derek 0493721068</p>
      <p class="location">Based in Brisbane QLD</p>
    </div>
  </section>

  <div class="presentation-notes">
    <p>One-sided business card<br>with logo design</p>
    <p>Plaster texture in logo</p>
  </div>

  <div class="logo-badge">
    <svg width="310" height="310" viewBox="0 0 310 310">
      <circle cx="155" cy="155" r="148" fill="var(--mark-fill)" stroke="var(--mark)" stroke-width="14"/>
      <text x="155" y="164" text-anchor="middle" font-family="Arimo, Arial, sans-serif"
            font-size="26" font-weight="500" fill="var(--mark)" letter-spacing="1">ND SERVICES QLD</text>
    </svg>
  </div>
</main>
</body>
</html>
```